Family Ranch with a hobby vineyard needs 2 wine labels for our first harvest

Design 2 wine labels (front and back) with the Brindor Ranch logo.
Label 1:
Sauvignon Blanc
Alc. 12.5% by Vol.
Palos Verdes Peninsula - add as the region
Year 2022
Label 2:
Cabernet Sauvignon
Alc. 13.5% by Vol.
Year 2022
For the back label design:
GOVERNMENT WARNING: (1) According to the Surgeon General, women
should not drink alcoholic beverages during pregnancy because of the risk of
birth defects. (2) Consumption of alcoholic beverages impairs your ability to
drive a car or operate machinery, and may cause health problems.
Contains Sulfates.
750ML
I just received the bottles and have attached a picture.
Look and feel
Each slider illustrates characteristics of the customer's brand and the style your logo design should communicate.

```html
<!DOCTYPE html>
<html lang="en">
<head>
<meta charset="utf-8">
<title>Brindor Ranch Wine Labels</title>
<link href="https://fonts.googleapis.com/css2?family=Poppins:wght@300;400;500;600&family=Cinzel:wght@400&display=swap" rel="stylesheet">
<style>
  :root {
    --board: #000000;
    --paper: #ffffff;
    --ink: #111111;
    --title: #ffffff;
    --gold: #c8912e;
    --vine-light: #f1f1f1;
    --vine-dark: #d6d6d6;
  }
  * { margin: 0; padding: 0; box-sizing: border-box; }
  html, body { width: 1200px; height: 1000px; overflow: hidden; background: var(--board); }
  .board { position: relative; width: 1200px; height: 1000px; background: var(--board); font-family: "Poppins", sans-serif; color: var(--ink); }

  .set-title { position: absolute; width: 240px; margin-left: -120px; text-align: center; color: var(--title); font-family: "Poppins", sans-serif; font-weight: 300; font-size: 22px; line-height: 1; }

  .label { position: absolute; }
  .label-front { width: 197px; height: 399px; }
  .label-back { width: 175px; height: 358px; }
  .label-shape { position: absolute; inset: 0; width: 100%; height: 100%; }

  .row { position: absolute; left: 0; right: 0; text-align: center; }
  .rating { display: flex; justify-content: center; gap: 2px; }
  .rating svg { display: block; }
  .quality { font-family: "Cinzel", serif; font-size: 8.5px; letter-spacing: 0.2px; line-height: 1; }

  .brand-dot { position: absolute; left: 50%; width: 44px; height: 44px; margin-left: -22px; border: 2px solid var(--ink); border-radius: 50%; }
  .brand-name { font-family: "Poppins", sans-serif; font-weight: 500; color: var(--ink); line-height: 1; text-transform: uppercase; }
  .label-front .brand-name.main { font-size: 25px; letter-spacing: 0.5px; }
  .label-front .brand-name.sub { font-size: 11px; letter-spacing: 6px; padding-left: 6px; }
  .label-back .brand-name.main { font-size: 21px; letter-spacing: 0.4px; }
  .label-back .brand-name.sub { font-size: 9px; letter-spacing: 5px; padding-left: 5px; }

  .wine-info { font-size: 5px; line-height: 6px; font-weight: 400; }
  .volume { font-size: 10px; font-weight: 500; line-height: 1; }
  .warning-title { font-size: 8.5px; font-weight: 500; line-height: 1; }
  .warning-text { left: 38px; right: 38px; font-size: 4.8px; line-height: 5.8px; }
  .warning-text p + p { margin-top: 6px; }
  .sulfates { font-size: 4.8px; line-height: 1; }
</style>
</head>
<body>
<main class="board">

  <h2 class="set-title" style="left:487px; top:42px;">Labels 1 Front</h2>
  <h2 class="set-title" style="left:723px; top:42px;">Back</h2>
  <h2 class="set-title" style="left:487px; top:515px;">Labels 2 Front</h2>
  <h2 class="set-title" style="left:723px; top:515px;">Back</h2>

  <!-- Sauvignon Blanc front -->
  <section class="label label-front" style="left:389px; top:92px;">
    <svg class="label-shape" viewBox="0 0 197 399" role="img" aria-label="Arched label with grapevine and leaf engraving around the border">
      <defs>
        <linearGradient id="vineFront1" x1="0" y1="0" x2="0" y2="1">
          <stop offset="0" stop-color="var(--vine-dark)"/>
          <stop offset="0.5" stop-color="var(--vine-light)"/>
          <stop offset="1" stop-color="var(--vine-dark)"/>
        </linearGradient>
      </defs>
      <path d="M0 40 C36 40 42 0 98.5 0 C155 0 161 40 197 40 L197 399 Q98.5 371 0 399 Z" fill="url(#vineFront1)"/>
      <path d="M13 54 C40 54 50 18 98.5 18 C147 18 157 54 184 54 L184 382 Q98.5 360 13 382 Z" fill="var(--paper)" stroke="var(--ink)" stroke-width="1"/>
    </svg>
    <div class="row rating" style="top:57px;">
      <svg width="7" height="7" viewBox="0 0 10 10"><polygon points="5,0 6.2,3.6 10,3.6 6.9,5.8 8.1,9.5 5,7.2 1.9,9.5 3.1,5.8 0,3.6 3.8,3.6" fill="var(--gold)"/></svg>
      <svg width="7" height="7" viewBox="0 0 10 10"><polygon points="5,0 6.2,3.6 10,3.6 6.9,5.8 8.1,9.5 5,7.2 1.9,9.5 3.1,5.8 0,3.6 3.8,3.6" fill="var(--gold)"/></svg>
      <svg width="10" height="10" viewBox="0 0 10 10"><polygon points="5,0 6.2,3.6 10,3.6 6.9,5.8 8.1,9.5 5,7.2 1.9,9.5 3.1,5.8 0,3.6 3.8,3.6" fill="var(--gold)"/></svg>
      <svg width="7" height="7" viewBox="0 0 10 10"><polygon points="5,0 6.2,3.6 10,3.6 6.9,5.8 8.1,9.5 5,7.2 1.9,9.5 3.1,5.8 0,3.6 3.8,3.6" fill="var(--gold)"/></svg>
      <svg width="7" height="7" viewBox="0 0 10 10"><polygon points="5,0 6.2,3.6 10,3.6 6.9,5.8 8.1,9.5 5,7.2 1.9,9.5 3.1,5.8 0,3.6 3.8,3.6" fill="var(--gold)"/></svg>
    </div>
    <p class="row quality" style="top:70px;">Premium Quality</p>
    <span class="brand-dot" style="top:140px;"></span>
    <p class="row brand-name main" style="top:205px;">Brindor</p>
    <p class="row brand-name sub" style="top:236px;">Ranch</p>
    <p class="row wine-info" style="top:292px;">Sauvignon Blanc<br>Alc. 12.5% by Vol.<br>Palos Verdes Peninsula - add as the region<br>Year 2022</p>
    <p class="row volume" style="top:339px;">750ML</p>
  </section>

  <!-- Sauvignon Blanc back -->
  <section class="label label-back" style="left:636px; top:132px;">
    <svg class="label-shape" viewBox="0 0 175 358" role="img" aria-label="Label with grapevine and leaf engraving around the border">
      <defs>
        <linearGradient id="vineBack1" x1="0" y1="0" x2="0" y2="1">
          <stop offset="0" stop-color="var(--vine-dark)"/>
          <stop offset="0.5" stop-color="var(--vine-light)"/>
          <stop offset="1" stop-color="var(--vine-dark)"/>
        </linearGradient>
      </defs>
      <rect width="175" height="358" fill="url(#vineBack1)"/>
      <rect x="13" y="13" width="149" height="333" rx="4" fill="var(--paper)" stroke="var(--ink)" stroke-width="1"/>
    </svg>
    <div class="row rating" style="top:40px;">
      <svg width="7" height="7" viewBox="0 0 10 10"><polygon points="5,0 6.2,3.6 10,3.6 6.9,5.8 8.1,9.5 5,7.2 1.9,9.5 3.1,5.8 0,3.6 3.8,3.6" fill="var(--gold)"/></svg>
      <svg width="7" height="7" viewBox="0 0 10 10"><polygon points="5,0 6.2,3.6 10,3.6 6.9,5.8 8.1,9.5 5,7.2 1.9,9.5 3.1,5.8 0,3.6 3.8,3.6" fill="var(--gold)"/></svg>
      <svg width="10" height="10" viewBox="0 0 10 10"><polygon points="5,0 6.2,3.6 10,3.6 6.9,5.8 8.1,9.5 5,7.2 1.9,9.5 3.1,5.8 0,3.6 3.8,3.6" fill="var(--gold)"/></svg>
      <svg width="7" height="7" viewBox="0 0 10 10"><polygon points="5,0 6.2,3.6 10,3.6 6.9,5.8 8.1,9.5 5,7.2 1.9,9.5 3.1,5.8 0,3.6 3.8,3.6" fill="var(--gold)"/></svg>
      <svg width="7" height="7" viewBox="0 0 10 10"><polygon points="5,0 6.2,3.6 10,3.6 6.9,5.8 8.1,9.5 5,7.2 1.9,9.5 3.1,5.8 0,3.6 3.8,3.6" fill="var(--gold)"/></svg>
    </div>
    <p class="row quality" style="top:53px;">Premium Quality</p>
    <p class="row brand-name main" style="top:102px;">Brindor</p>
    <p class="row brand-name sub" style="top:126px;">Ranch</p>
    <p class="row warning-title" style="top:189px;">GOVERNMENT WARNING</p>
    <div class="row warning-text" style="top:210px;">
      <p>(1) According to the Surgeon General, women should not drink alcoholic beverages during pregnancy because of the risk of birth defects.</p>
      <p>(2) Consumption of alcoholic beverages impairs your ability to drive a car or operate machinery, and may cause health problems.</p>
    </div>
    <p class="row sulfates" style="top:287px;">Contains Sulfates.</p>
    <p class="row volume" style="top:316px;">750ML</p>
  </section>

  <!-- Cabernet Sauvignon front -->
  <section class="label label-front" style="left:389px; top:559px;">
    <svg class="label-shape" viewBox="0 0 197 399" role="img" aria-label="Arched label with grapevine and leaf engraving around the border">
      <defs>
        <linearGradient id="vineFront2" x1="0" y1="0" x2="0" y2="1">
          <stop offset="0" stop-color="var(--vine-dark)"/>
          <stop offset="0.5" stop-color="var(--vine-light)"/>
          <stop offset="1" stop-color="var(--vine-dark)"/>
        </linearGradient>
      </defs>
      <path d="M0 40 C36 40 42 0 98.5 0 C155 0 161 40 197 40 L197 399 Q98.5 371 0 399 Z" fill="url(#vineFront2)"/>
      <path d="M13 54 C40 54 50 18 98.5 18 C147 18 157 54 184 54 L184 382 Q98.5 360 13 382 Z" fill="var(--paper)" stroke="var(--ink)" stroke-width="1"/>
    </svg>
    <div class="row rating" style="top:57px;">
      <svg width="7" height="7" viewBox="0 0 10 10"><polygon points="5,0 6.2,3.6 10,3.6 6.9,5.8 8.1,9.5 5,7.2 1.9,9.5 3.1,5.8 0,3.6 3.8,3.6" fill="var(--gold)"/></svg>
      <svg width="7" height="7" viewBox="0 0 10 10"><polygon points="5,0 6.2,3.6 10,3.6 6.9,5.8 8.1,9.5 5,7.2 1.9,9.5 3.1,5.8 0,3.6 3.8,3.6" fill="var(--gold)"/></svg>
      <svg width="10" height="10" viewBox="0 0 10 10"><polygon points="5,0 6.2,3.6 10,3.6 6.9,5.8 8.1,9.5 5,7.2 1.9,9.5 3.1,5.8 0,3.6 3.8,3.6" fill="var(--gold)"/></svg>
      <svg width="7" height="7" viewBox="0 0 10 10"><polygon points="5,0 6.2,3.6 10,3.6 6.9,5.8 8.1,9.5 5,7.2 1.9,9.5 3.1,5.8 0,3.6 3.8,3.6" fill="var(--gold)"/></svg>
      <svg width="7" height="7" viewBox="0 0 10 10"><polygon points="5,0 6.2,3.6 10,3.6 6.9,5.8 8.1,9.5 5,7.2 1.9,9.5 3.1,5.8 0,3.6 3.8,3.6" fill="var(--gold)"/></svg>
    </div>
    <p class="row quality" style="top:70px;">Premium Quality</p>
    <span class="brand-dot" style="top:140px;"></span>
    <p class="row brand-name main" style="top:205px;">Brindor</p>
    <p class="row brand-name sub" style="top:236px;">Ranch</p>
    <p class="row wine-info" style="top:292px;">Cabernet Sauvignon<br>Alc. 13.5% by Vol.<br>Palos Verdes Peninsula - add as the region<br>Year 2022</p>
    <p class="row volume" style="top:339px;">750ML</p>
  </section>

  <!-- Cabernet Sauvignon back -->
  <section class="label label-back" style="left:636px; top:599px;">
    <svg class="label-shape" viewBox="0 0 175 358" role="img" aria-label="Label with grapevine and leaf engraving around the border">
      <defs>
        <linearGradient id="vineBack2" x1="0" y1="0" x2="0" y2="1">
          <stop offset="0" stop-color="var(--vine-dark)"/>
          <stop offset="0.5" stop-color="var(--vine-light)"/>
          <stop offset="1" stop-color="var(--vine-dark)"/>
        </linearGradient>
      </defs>
      <rect width="175" height="358" fill="url(#vineBack2)"/>
      <rect x="13" y="13" width="149" height="333" rx="4" fill="var(--paper)" stroke="var(--ink)" stroke-width="1"/>
    </svg>
    <div class="row rating" style="top:40px;">
      <svg width="7" height="7" viewBox="0 0 10 10"><polygon points="5,0 6.2,3.6 10,3.6 6.9,5.8 8.1,9.5 5,7.2 1.9,9.5 3.1,5.8 0,3.6 3.8,3.6" fill="var(--gold)"/></svg>
      <svg width="7" height="7" viewBox="0 0 10 10"><polygon points="5,0 6.2,3.6 10,3.6 6.9,5.8 8.1,9.5 5,7.2 1.9,9.5 3.1,5.8 0,3.6 3.8,3.6" fill="var(--gold)"/></svg>
      <svg width="10" height="10" viewBox="0 0 10 10"><polygon points="5,0 6.2,3.6 10,3.6 6.9,5.8 8.1,9.5 5,7.2 1.9,9.5 3.1,5.8 0,3.6 3.8,3.6" fill="var(--gold)"/></svg>
      <svg width="7" height="7" viewBox="0 0 10 10"><polygon points="5,0 6.2,3.6 10,3.6 6.9,5.8 8.1,9.5 5,7.2 1.9,9.5 3.1,5.8 0,3.6 3.8,3.6" fill="var(--gold)"/></svg>
      <svg width="7" height="7" viewBox="0 0 10 10"><polygon points="5,0 6.2,3.6 10,3.6 6.9,5.8 8.1,9.5 5,7.2 1.9,9.5 3.1,5.8 0,3.6 3.8,3.6" fill="var(--gold)"/></svg>
    </div>
    <p class="row quality" style="top:53px;">Premium Quality</p>
    <p class="row brand-name main" style="top:102px;">Brindor</p>
    <p class="row brand-name sub" style="top:126px;">Ranch</p>
    <p class="row warning-title" style="top:189px;">GOVERNMENT WARNING</p>
    <div class="row warning-text" style="top:210px;">
      <p>(1) According to the Surgeon General, women should not drink alcoholic beverages during pregnancy because of the risk of birth defects.</p>
      <p>(2) Consumption of alcoholic beverages impairs your ability to drive a car or operate machinery, and may cause health problems.</p>
    </div>
    <p class="row sulfates" style="top:287px;">Contains Sulfates.</p>
    <p class="row volume" style="top:316px;">750ML</p>
  </section>

</main>
</body>
</html>
```